I will ask the design of the business card

We are looking for business card design of the new company "VORTELL PAYWORKS STUDIO LLC." Based in Azerbaijan.
In case
We are working on Azerbaijan to set up the first exchange of crypto currencies.

The key currency used in exchanges is called "MIRTA".
In case
We are doing project to make crypto currency infrastructure.

We provide state-of-the-art technology to the world.

```html
<!DOCTYPE html>
<html lang="en">
<head>
<meta charset="utf-8">
<title>Vortell Payworks Studio LLC. – Business Card</title>
<link rel="stylesheet" href="https://fonts.googleapis.com/css2?family=Michroma&display=swap">
<style>
  :root {
    --backdrop: #2a2a2c;
    --brand-blue: #2f2f9c;
    --brand-blue-light: #4646b8;
    --brand-navy: #2b2b8f;
    --brand-orange: #f28a1e;
    --card-white: #ffffff;
  }
  * { box-sizing: border-box; margin: 0; padding: 0; }
  html, body { width: 1200px; height: 902px; overflow: hidden; }
  body {
    background: var(--backdrop);
    font-family: "Michroma", "Arial", sans-serif;
    position: relative;
  }
  .card {
    position: absolute;
    left: 267px;
    width: 666px;
    height: 380px;
    border-radius: 4px;
    overflow: hidden;
    box-shadow: 0 10px 28px rgba(0,0,0,.45);
  }
  /* Front side */
  .card--front {
    top: 50px;
    background: linear-gradient(135deg, var(--brand-blue) 0%, var(--brand-blue-light) 100%);
    display: flex;
    align-items: center;
    justify-content: center;
  }
  .brand-lockup {
    display: flex;
    align-items: center;
    gap: 16px;
  }
  .brand-lockup__dot {
    width: 42px; height: 42px;
    border-radius: 50%;
    background: var(--brand-orange);
    flex: none;
  }
  .brand-lockup__name {
    font-size: 19px;
    line-height: 1.35;
    letter-spacing: .5px;
    color: var(--card-white);
  }
  /* Back side */
  .card--back {
    top: 472px;
    background: var(--card-white);
  }
  .card--back .brand-lockup {
    position: absolute;
    right: 38px; top: 44px;
    gap: 12px;
  }
  .card--back .brand-lockup__dot { width: 34px; height: 34px; }
  .card--back .brand-lockup__name {
    color: var(--brand-navy);
    font-size: 14px;
    text-align: left;
  }
  .address {
    position: absolute;
    right: 40px; top: 130px;
    width: 270px;
    padding-top: 12px;
    border-top: 2px solid var(--brand-orange);
    text-align: right;
    color: var(--brand-navy);
    font-size: 11px;
    line-height: 1.7;
  }
  .person {
    position: absolute;
    left: 38px; top: 150px;
  }
  .person__name {
    color: var(--brand-navy);
    font-size: 24px;
    font-weight: 400;
    letter-spacing: .5px;
  }
  .person__role {
    color: var(--brand-orange);
    font-size: 13px;
    margin-top: 4px;
  }
  .divider {
    position: absolute;
    left: 38px; top: 232px;
    width: 330px; height: 2px;
    background: var(--brand-navy);
  }
  .contacts {
    position: absolute;
    left: 38px; top: 250px;
    list-style: none;
  }
  .contacts li {
    display: flex;
    align-items: center;
    gap: 12px;
    height: 26px;
    color: var(--brand-navy);
    font-size: 12px;
  }
  .contacts svg { width: 18px; height: 18px; flex: none; }
</style>
</head>
<body>

<section class="card card--front" aria-label="Business card front">
  <div class="brand-lockup">
    <span class="brand-lockup__dot"></span>
    <span class="brand-lockup__name">VORTELL PAYWORKS<br>STUDIO LLC.</span>
  </div>
</section>

<section class="card card--back" aria-label="Business card back">
  <div class="brand-lockup">
    <span class="brand-lockup__dot"></span>
    <span class="brand-lockup__name">VORTELL PAYWORKS<br>STUDIO LLC.</span>
  </div>

  <p class="address">14 Nizami Street, Suite 210<br>Baku, AZ 1000</p>

  <div class="person">
    <h1 class="person__name">ELIN MARR</h1>
    <p class="person__role">MANAGING DIRECTOR</p>
  </div>

  <div class="divider"></div>

  <ul class="contacts">
    <li>
      <svg viewBox="0 0 18 18"><rect width="18" height="18" rx="3" fill="#f28a1e"/><path d="M5 4.5c.6-.6 1.4-.6 1.8 0l1 1.4c.3.5.2 1-.2 1.4l-.6.6c.5 1.1 1.3 1.9 2.4 2.4l.6-.6c.4-.4 1-.5 1.4-.2l1.4 1c.6.4.6 1.2 0 1.8l-.7.7C10.6 14 4 7.4 4.3 5.2z" fill="#fff"/></svg>
      +994 12 555 3170
    </li>
    <li>
      <svg viewBox="0 0 18 18"><rect width="18" height="18" rx="3" fill="#f28a1e"/><rect x="6" y="3.5" width="6" height="3.5" fill="#fff"/><rect x="3.5" y="7" width="11" height="5" rx="1" fill="#fff"/><rect x="6" y="10.5" width="6" height="4" fill="#fff" stroke="#f28a1e" stroke-width=".8"/></svg>
      +994 12 555 4291
    </li>
    <li>
      <svg viewBox="0 0 18 18"><rect width="18" height="18" rx="3" fill="#f28a1e"/><rect x="3.5" y="5" width="11" height="8" fill="none" stroke="#fff" stroke-width="1.4"/><path d="M3.5 5l5.5 4.5L14.5 5" fill="none" stroke="#fff" stroke-width="1.4"/></svg>
      info@vortellpayworks.az
    </li>
    <li>
      <svg viewBox="0 0 18 18"><rect width="18" height="18" rx="3" fill="#f28a1e"/><circle cx="9" cy="9" r="5.2" fill="none" stroke="#fff" stroke-width="1.2"/><ellipse cx="9" cy="9" rx="2.2" ry="5.2" fill="none" stroke="#fff" stroke-width="1"/><path d="M3.8 9h10.4" stroke="#fff" stroke-width="1"/></svg>
      www.vortellpayworks.az
    </li>
  </ul>
</section>

</body>
</html>
```